VR Business Card

Design new business cards for VELMOsoft

Please see attached for the design brief

**** Please note, please feel free to propose a font that works for a professional, technology company ***

Target Market(s)

Technology buyers

Industry/Entity Type

Business

```html
<!DOCTYPE html>
<html lang="en">
<head>
<meta charset="utf-8">
<title>VELMOsoft Business Card</title>
<link rel="stylesheet" href="https://fonts.googleapis.com/css2?family=Arimo:wght@400;700&display=swap">
<style>
  :root {
    --backdrop: #8a8a8a;
    --card-dark: #0c1a22;
    --card-white: #f4f4f4;
    --ink-navy: #23317a;
    --ink-light: #d9dde0;
    --ink-grey: #5a5f63;
    --ink-body: #2b2f33;
    --accent-orange: #e69a1c;
    --accent-blue: #4a6fb5;
    --accent-teal: #137563;
    --accent-purple: #5a4ea3;
    --link-blue: #6f8fd6;
  }
  html, body {
    margin: 0;
    padding: 0;
    width: 1200px;
    height: 1000px;
    overflow: hidden;
    background: var(--backdrop);
    font-family: "Arimo", Arial, sans-serif;
  }
  .canvas {
    position: relative;
    width: 1200px;
    height: 1000px;
  }
  .card {
    position: absolute;
    left: 330px;
    width: 540px;
    height: 320px;
    box-shadow: 0 8px 24px rgba(0,0,0,0.35);
    overflow: hidden;
  }
  .card-back { top: 120px; background: var(--card-dark); }
  .card-front { top: 540px; background: var(--card-white); }

  .wordmark {
    position: absolute;
    display: flex;
    align-items: center;
    gap: 10px;
    font-size: 34px;
    font-weight: 700;
    letter-spacing: 0.5px;
    white-space: nowrap;
  }
  .wordmark-square { width: 16px; height: 16px; background: var(--accent-blue); }
  .card-back .wordmark { left: 34px; top: 46px; color: var(--ink-light); }
  .card-front .wordmark { left: 30px; top: 30px; color: var(--ink-navy); }

  .tagline { position: absolute; left: 300px; font-size: 14px; white-space: nowrap; }
  .card-back .tagline { top: 52px; color: var(--accent-orange); }
  .card-front .tagline { top: 80px; color: var(--ink-grey); }

  .company-address {
    position: absolute;
    left: 300px;
    top: 168px;
    margin: 0;
    font-style: normal;
    font-size: 14px;
    line-height: 17px;
    color: var(--ink-light);
  }
  .company-web { display: block; margin-top: 6px; color: var(--link-blue); }

  .identity-band {
    position: absolute;
    left: 0; top: 118px;
    width: 540px; height: 64px;
    background: linear-gradient(90deg, var(--card-dark) 60%, #2c363d 100%);
  }
  .accent-stripe { position: absolute; top: 182px; left: 0; display: flex; height: 5px; width: 540px; }
  .accent-stripe span { width: 46px; }
  .accent-stripe .blue { background: var(--accent-blue); }
  .accent-stripe .orange { background: var(--accent-orange); }
  .accent-stripe .teal { background: var(--accent-teal); }
  .accent-stripe .purple { background: var(--accent-purple); }
  .accent-stripe .rest { flex: 1; background: var(--card-dark); }

  .person-name { position: absolute; left: 30px; top: 130px; margin: 0; font-size: 19px; font-weight: 700; color: #fff; }
  .person-role { position: absolute; left: 30px; top: 154px; font-size: 11px; color: var(--ink-light); }
  .person-direct {
    position: absolute; left: 270px; top: 132px;
    font-size: 13px; line-height: 17px; color: #fff;
    white-space: nowrap;
  }

  .office-lines {
    position: absolute; left: 270px; top: 222px;
    margin: 0; padding: 0; list-style: none;
    font-size: 14px; line-height: 17px; color: var(--ink-body);
    white-space: nowrap;
  }
  .office-lines .label { color: var(--accent-orange); margin-left: 4px; }
</style>
</head>
<body>
<main class="canvas">
  <section class="card card-back" aria-label="Card back">
    <div class="wordmark"><span class="wordmark-square"></span>VELMOsoft</div>
    <div class="tagline">...progress is our craft</div>
    <address class="company-address">
      VELMOsoft Solutions AG<br>
      Seeweg 8<br>
      6300 Lindenau<br>
      Switzerland
      <span class="company-web">www.velmosoft-it.example</span>
    </address>
  </section>

  <section class="card card-front" aria-label="Card front">
    <div class="wordmark"><span class="wordmark-square"></span>VELMOsoft</div>
    <div class="tagline">...progress is our craft</div>
    <div class="identity-band"></div>
    <div class="accent-stripe">
      <span class="blue"></span><span class="orange"></span><span class="teal"></span><span class="purple"></span><span class="rest"></span>
    </div>
    <h1 class="person-name">Martin Alder</h1>
    <div class="person-role">CEO</div>
    <div class="person-direct">
      +41 79 5550123<br>
      martin.alder@velmosoft-it.example
    </div>
    <ul class="office-lines">
      <li>+41 41 555 01 20<span class="label">phone</span></li>
      <li>+41 41 555 01 21<span class="label">direct</span></li>
      <li>+41 800 555 014<span class="label">fax</span></li>
    </ul>
  </section>
</main>
</body>
</html>
```